Redesign/Facelift for Affiliate Shopping Fashion Site

We are velunix, Fashion web site from Berlin, Germany,
looking to redesign/facelift our affiliate shopping site,
http://shop.velunix.de/bekleidung,84rtpa21xuwdnc90,ec_sale,sa
(Main page view)
http://shop.velunix.de/lorn-gale-seidentunika-pemby,3kdh5w1rcyt8ae6v,i
(Single article view)

Altogether we want to make it more coherent, key words being
MINIMAL and STYLISH.

NOTE:
You don´t need to completely design both pages, it would be sufficient to propose a direction you would take. However, we should be able to envision the complete solution.

The solution should be similar to another comparable affiliate site,
http://www.kaufzirkel.de/browse/damen-kleidung

- - General Brief:
The design should have an overall aesthetic coherence,
especially when it comes to sizes of elements
and the bars like in the side bar left, or "Zum Shop".
The solution should be done for the main page and the single article page.

- - Here are the elements in particular, and how they should be designed:
- Main Page HEADER BAR (and single article page) elements:
header bar extends across the entire width of the screen
our logo
"Shopping" text next to the logo
search form
categories "Bekleidung, Accessoires, Schmuck" etc.
Plimbora and zappel buttons

- Main page SIDEBAR (left):
elements as can be seen
menu "Preis" is replaced by a price "slider" to more accurately determine
a shopping price range

- Main page PRODUCTS:
elements as can be seen
the "% discount" symbol and "Zum Shop" elements especially
should be looked at

- Main page (and single article page) FOOTER:
should extend across the entire width of the screen

- Single article page
(http://shop.velunix.de/lorn-gale-seidentunika-pemby,3kdh5w1rcyt8ae6v,i)
header and footer as discussed for the Main page
bars (below the article) "Ähnliche Produkte zu….", "Weitere Produkte…" should be replaced by
"lighter" solution

Thank you,
feel free to ask question if something is not clear.
Telmo

```html
<!DOCTYPE html>
<html lang="de">
<head>
<meta charset="utf-8">
<title>velunix – Bekleidung</title>
<link rel="stylesheet" href="https://fonts.googleapis.com/css2?family=Montserrat:wght@400;600;700&family=Noto+Serif:wght@400&display=swap">
<style>
:root{
  --ink:#1c1c1c;
  --black:#111;
  --head-top:#262626;
  --head-bottom:#0b0b0b;
  --accent:#ff4458;
  --grey:#8a8a8a;
  --light:#e6e6e6;
  --line:#dcdcdc;
  --bg:#ffffff;
  --white:#ffffff;
}
*{box-sizing:border-box;margin:0;padding:0}
html,body{width:1200px;height:2542px;overflow:hidden;background:var(--bg);font-family:"Montserrat",Arial,sans-serif;color:var(--ink)}
.page{position:relative;width:1200px;height:2542px;overflow:hidden}

/* header */
.masthead{position:absolute;left:0;top:0;width:1200px;height:100px;background:linear-gradient(var(--head-top),var(--head-bottom));border-top:4px solid var(--accent)}
.brand{position:absolute;left:73px;top:40px;color:var(--white);font-weight:700;font-size:25px;letter-spacing:.5px;text-transform:uppercase}
.social{position:absolute;right:66px;top:24px;display:flex;gap:22px}
.social span{width:14px;height:14px;border-radius:50%;background:var(--white);display:block}
.toplinks{position:absolute;right:66px;top:68px;display:flex;gap:14px;font-size:9px;font-weight:700;color:var(--white);text-transform:uppercase}
.toplinks span+span{border-left:1px solid #555;padding-left:14px}
.catnav{position:absolute;left:0;top:100px;width:1200px;height:45px;background:linear-gradient(#2b2b2b,#161616)}
.catnav ul{list-style:none}
.catnav li{position:absolute;top:0;line-height:45px;font-size:11px;font-weight:600;color:#ddd;letter-spacing:.5px;text-transform:uppercase;white-space:nowrap}
.catnav li.is-active{color:var(--white);font-weight:700}
.catnav li .plus{color:var(--accent);margin-left:8px}
.search{position:absolute;left:905px;top:10px;width:196px;height:26px;background:var(--white);border-radius:2px;font-size:8px;color:var(--grey);padding:9px 16px;font-weight:600;text-transform:uppercase;white-space:nowrap}
.search svg{position:absolute;right:10px;top:6px}

/* sidebar */
.sidebar{position:absolute;left:71px;top:176px;width:175px}
.side-title{font-size:11px;font-weight:700;text-transform:uppercase;letter-spacing:.3px;padding-bottom:8px;border-bottom:1px solid var(--light)}
.radio{display:flex;align-items:center;font-size:10px;margin:10px 0 0 14px}
.radio i{width:10px;height:10px;border-radius:50%;background:var(--light);margin-right:14px}
.price{position:relative;height:70px;margin-top:8px}
.price .track{position:absolute;left:12px;right:12px;top:17px;height:3px;background:var(--light)}
.price .knob{position:absolute;top:11px;width:6px;height:14px;background:#c9c9c9;border-radius:2px}
.price .lbl{position:absolute;top:40px;font-size:10px}
.filter{display:flex;justify-content:space-between;font-size:9px;padding:8px 0 8px 2px;border-bottom:1px solid var(--light);margin-top:6px}
.list{position:relative;list-style:none;padding-right:18px}
.list::after{content:"";position:absolute;right:0;top:4px;width:7px;height:52px;background:var(--light)}
.list::before{content:"";position:absolute;right:3px;top:4px;bottom:4px;width:1px;background:var(--light)}
.list li{font-size:10px;padding:0 0 0 12px;height:25.8px;line-height:25.8px;text-transform:uppercase;white-space:nowrap}
.list li.is-current{background:#f3f3f3}
.list li.two{line-height:14px;height:38px;padding-top:4px}
.check{display:flex;align-items:center;font-size:9px;margin:10px 0 0 10px}
.check i{width:9px;height:9px;border:1px solid #bbb;margin-right:10px}
.section{margin-top:26px}

/* content */
.crumb{position:absolute;left:287px;top:176px;width:867px;font-size:10px;color:#666;padding-bottom:10px;border-bottom:1px solid var(--light)}
.crumb b{color:var(--accent);font-weight:400}
.headline{position:absolute;left:287px;top:216px;font-family:"Noto Serif",Georgia,serif;font-size:19px;font-weight:400;color:#444}
.tools{position:absolute;left:775px;top:220px;display:flex;align-items:center;font-size:8px;color:#666}
.tools i{width:10px;height:10px;border:1px solid #ccc;margin-right:10px}
.tools .sort{margin-left:34px}
.tools .select{margin-left:14px;width:124px;height:22px;border:1px solid #ccc;background:#f1f1f1;display:flex;align-items:center;padding-left:12px;font-weight:600;position:relative}
.tools .select::after{content:"";position:absolute;right:8px;top:8px;border:4px solid transparent;border-top-color:#777}

.grid{position:absolute;left:287px;top:267px;display:grid;grid-template-columns:repeat(4,198px);column-gap:25px;row-gap:30px}
.card{position:relative;width:198px;height:338px;border:1px solid var(--line);background:var(--white)}
.photo{position:absolute;left:0;top:0;width:196px;height:204px}
.photo.cardigan{background:linear-gradient(180deg,#ffffff 0%,#ededed 55%,#8c8c8c 100%)}
.photo.blouse{background:linear-gradient(180deg,#ffffff 0%,#9aa17a 40%,#5f6a3e 75%,#202020 100%)}
.badge{position:absolute;right:-1px;top:-1px;width:62px;height:62px;background:var(--black);clip-path:polygon(0 0,100% 0,100% 100%)}
.badge span{position:absolute;right:5px;top:8px;color:var(--white);font-size:10px;font-weight:700}
.view{position:absolute;left:44px;top:90px;width:106px;height:28px;border-radius:14px;background:var(--accent);color:var(--white);font-size:11px;font-weight:700;text-align:center;line-height:28px;text-transform:uppercase}
.info{position:absolute;left:16px;top:210px;right:10px}
.cat{font-size:10px;color:var(--grey);text-transform:uppercase;letter-spacing:.3px}
.title{font-size:10.5px;font-weight:700;line-height:15px;margin-top:7px;text-transform:uppercase;white-space:nowrap;overflow:hidden}
.prices{font-size:12px;color:var(--accent);margin-top:6px;white-space:nowrap}
.prices .now{margin-left:16px}
.ship{font-size:9px;color:var(--grey);margin-top:7px;text-transform:uppercase}
.shop{position:absolute;left:-1px;right:-1px;bottom:-1px;height:24px;background:var(--accent);color:var(--white);font-size:12px;font-weight:700;text-align:center;line-height:24px}

.more{position:absolute;left:601px;top:2145px;width:203px;height:37px;border-radius:19px;background:var(--black);color:var(--white);font-size:12px;font-weight:600;text-align:center;line-height:37px;text-transform:uppercase}

/* footer */
.footer{position:absolute;left:0;top:2292px;width:1200px;height:250px;background:var(--black);color:var(--white)}
.footer .brand{left:97px;top:46px}
.blurb{position:absolute;left:97px;top:94px;width:280px;font-size:11px;line-height:20px;color:#9a9a9a;font-weight:600}
.copy{position:absolute;left:97px;top:166px;font-size:11px;line-height:20px;font-weight:700}
.fcol{position:absolute;top:50px;font-size:11px;line-height:22px;font-weight:600;color:#cfcfcf}
.fcol h4{font-size:12px;color:var(--white);font-weight:700;text-transform:uppercase;margin-bottom:10px;letter-spacing:.5px}
.signup{position:absolute;left:891px;top:50px}
.signup h4{font-size:12px;font-weight:700;text-transform:uppercase;letter-spacing:.5px}
.email{margin-top:22px;width:253px;height:37px;border-radius:19px;background:var(--white);display:flex;align-items:center;justify-content:space-between;padding:0 26px 0 20px;font-size:11px}
.email span{color:#aaa}
.email b{color:var(--ink);text-transform:uppercase;font-weight:700}
.signup .stay{margin-top:34px}
.fsocial{display:flex;gap:20px;margin-top:16px}
.fsocial i{width:14px;height:14px;border-radius:50%;background:var(--white)}
</style>
</head>
<body>
<div class="page">

  <header class="masthead">
    <div class="brand">velunix</div>
    <div class="social" aria-label="Soziale Netzwerke"><span title="Plimbora"></span><span title="zappel"></span><span title="Feed"></span></div>
    <nav class="toplinks"><span>News</span><span>velunix.tv</span><span>Selection</span><span>Fashion Art</span></nav>
  </header>
  <nav class="catnav">
    <ul>
      <li class="is-active" style="left:73px">Bekleidung</li>
      <li style="left:185px">Accessoires</li>
      <li style="left:303px">Schmuck</li>
      <li style="left:398px">Schuhe</li>
      <li style="left:481px">Taschen</li>
      <li style="left:570px">Uhren</li>
      <li style="left:646px">Beauty</li>
      <li style="left:728px">Wohnen</li>
      <li style="left:815px">More<span class="plus">+</span></li>
    </ul>
    <div class="search">Wonach suchst du?
      <svg width="14" height="14" viewBox="0 0 14 14"><circle cx="5.5" cy="5.5" r="4.2" fill="none" stroke="#ff4458" stroke-width="1.8"/><line x1="8.6" y1="8.6" x2="12.5" y2="12.5" stroke="#ff4458" stroke-width="2"/></svg>
    </div>
  </nav>

  <aside class="sidebar">
    <div class="side-title">Geschlecht</div>
    <div class="radio"><i></i>Männlich</div>
    <div class="radio"><i></i>Weiblich</div>

    <div class="section">
      <div class="side-title">Preis</div>
      <div class="price">
        <div class="track"></div>
        <div class="knob" style="left:16px"></div>
        <div class="knob" style="left:130px"></div>
        <div class="lbl" style="left:12px">5 €</div>
        <div class="lbl" style="left:116px">150 €</div>
      </div>
    </div>

    <div class="section" style="margin-top:6px">
      <div class="side-title">Kategorien</div>
      <div class="filter"><span>Filter Entfernen</span><span>×</span></div>
      <ul class="list">
        <li class="is-current">Bekleidung (198139)</li><li>Anzüge (139)</li><li>Bademode (4636)</li><li>Blazer (968)</li><li>Blusen (2962)</li><li>Wäsche (3501)</li><li>Hemden (7899)</li><li>Homewear (99)</li><li>Hosen (42339)</li><li>Jacken (15524)</li>
      </ul>
    </div>

    <div class="section">
      <div class="side-title">Marken</div>
      <div class="filter"><span>Filter Entfernen</span><span>×</span></div>
      <ul class="list">
        <li>9 Für Jeden Tag (421)</li><li>8.4 By Dario Fenelli (416)</li><li>KTR (393)</li><li>Orla Moda (850)</li><li>Benedetta R. (429)</li><li>Avorn (417)</li><li>Nevado (414)</li><li>Elmo Maternity (374)</li><li>Varesi (384)</li><li class="two">R.T. Real Threads<br>(1508)</li>
      </ul>
    </div>

    <div class="section" style="margin-top:14px">
      <div class="side-title">% Sale %</div>
      <div class="check"><i></i>Nur reduzierte Artikel</div>
    </div>

    <div class="section">
      <div class="side-title">Material</div>
      <div class="filter"><span>Filter Entfernen</span><span>×</span></div>
      <ul class="list">
        <li>Pelz (121682)</li><li>Jersey (35068)</li><li>Tuch (31660)</li><li>Stretch (29588)</li><li>Blei (29167)</li><li>Baumwolle (19998)</li><li>Denim (19858)</li><li>Krepp (13945)</li><li>Polyester (11257)</li><li>Gabardine (8711)</li>
      </ul>
    </div>
  </aside>

  <div class="crumb"><b>START</b> &gt; Bekleidung</div>
  <h1 class="headline">Find Discounts up to: 70%</h1>
  <div class="tools"><i></i>Nur reduzierte Artikel<span class="sort">Sortieren nach:</span><span class="select">BELIEBTESTE</span></div>

  <main class="grid">
    <article class="card"><div class="photo cardigan" role="img" aria-label="Produktfoto: Model in weißer Strickjacke und grauer Jeans"></div><div class="badge"><span>-45%</span></div><div class="view">View Item</div><div class="info"><div class="cat">Cardingans</div><div class="title">Storehall - Strukturk<br>leid mit Rückwärtigem...</div><div class="prices">65.00€<span class="now">€ 24.99 €*</span></div><div class="ship">Versand: +5,95</div></div><div class="shop">Zum Shop</div></article>
    <article class="card"><div class="photo blouse" role="img" aria-label="Produktfoto: Model in olivgrüner Bluse und schwarzer Hose"></div><div class="badge"><span>-31%</span></div><div class="info"><div class="cat">Cardingans</div><div class="title">Storehall - Strukturk<br>leid mit Rückwärtigem...</div><div class="prices">65.00€<span class="now">€ 24.99 €*</span></div><div class="ship">Versand: +5,95</div></div><div class="shop">Zum Shop</div></article>
    <article class="card"><div class="photo cardigan" role="img" aria-label="Produktfoto: Model in weißer Strickjacke und grauer Jeans"></div><div class="badge"><span>-45%</span></div><div class="info"><div class="cat">Cardingans</div><div class="title">Storehall - Strukturk<br>leid mit Rückwärtigem...</div><div class="prices">65.00€<span class="now">€ 24.99 €*</span></div><div class="ship">Versand: +5,95</div></div><div class="shop">Zum Shop</div></article>
    <article class="card"><div class="photo blouse" role="img" aria-label="Produktfoto: Model in olivgrüner Bluse und schwarzer Hose"></div><div class="badge"><span>-31%</span></div><div class="info"><div class="cat">Cardingans</div><div class="title">Storehall - Strukturk<br>leid mit Rückwärtigem...</div><div class="prices">65.00€<span class="now">€ 24.99 €*</span></div><div class="ship">Versand: +5,95</div></div><div class="shop">Zum Shop</div></article>

    <article class="card"><div class="photo cardigan" role="img" aria-label="Produktfoto: Model in weißer Strickjacke und grauer Jeans"></div><div class="badge"><span>-45%</span></div><div class="info"><div class="cat">Cardingans</div><div class="title">Storehall - Strukturk<br>leid mit Rückwärtigem...</div><div class="prices">65.00€<span class="now">€ 24.99 €*</span></div><div class="ship">Versand: +5,95</div></div><div class="shop">Zum Shop</div></article>
    <article class="card"><div class="photo blouse" role="img" aria-label="Produktfoto: Model in olivgrüner Bluse und schwarzer Hose"></div><div class="badge"><span>-31%</span></div><div class="info"><div class="cat">Cardingans</div><div class="title">Storehall - Strukturk<br>leid mit Rückwärtigem...</div><div class="prices">65.00€<span class="now">€ 24.99 €*</span></div><div class="ship">Versand: +5,95</div></div><div class="shop">Zum Shop</div></article>
    <article class="card"><div class="photo cardigan" role="img" aria-label="Produktfoto: Model in weißer Strickjacke und grauer Jeans"></div><div class="badge"><span>-45%</span></div><div class="info"><div class="cat">Cardingans</div><div class="title">Storehall - Strukturk<br>leid mit Rückwärtigem...</div><div class="prices">65.00€<span class="now">€ 24.99 €*</span></div><div class="ship">Versand: +5,95</div></div><div class="shop">Zum Shop</div></article>
    <article class="card"><div class="photo blouse" role="img" aria-label="Produktfoto: Model in olivgrüner Bluse und schwarzer Hose"></div><div class="badge"><span>-31%</span></div><div class="info"><div class="cat">Cardingans</div><div class="title">Storehall - Strukturk<br>leid mit Rückwärtigem...</div><div class="prices">65.00€<span class="now">€ 24.99 €*</span></div><div class="ship">Versand: +5,95</div></div><div class="shop">Zum Shop</div></article>

    <article class="card"><div class="photo cardigan" role="img" aria-label="Produktfoto: Model in weißer Strickjacke und grauer Jeans"></div><div class="badge"><span>-45%</span></div><div class="info"><div class="cat">Cardingans</div><div class="title">Storehall - Strukturk<br>leid mit Rückwärtigem...</div><div class="prices">65.00€<span class="now">€ 24.99 €*</span></div><div class="ship">Versand: +5,95</div></div><div class="shop">Zum Shop</div></article>
    <article class="card"><div class="photo blouse" role="img" aria-label="Produktfoto: Model in olivgrüner Bluse und schwarzer Hose"></div><div class="badge"><span>-31%</span></div><div class="info"><div class="cat">Cardingans</div><div class="title">Storehall - Strukturk<br>leid mit Rückwärtigem...</div><div class="prices">65.00€<span class="now">€ 24.99 €*</span></div><div class="ship">Versand: +5,95</div></div><div class="shop">Zum Shop</div></article>
    <article class="card"><div class="photo cardigan" role="img" aria-label="Produktfoto: Model in weißer Strickjacke und grauer Jeans"></div><div class="badge"><span>-45%</span></div><div class="info"><div class="cat">Cardingans</div><div class="title">Storehall - Strukturk<br>leid mit Rückwärtigem...</div><div class="prices">65.00€<span class="now">€ 24.99 €*</span></div><div class="ship">Versand: +5,95</div></div><div class="shop">Zum Shop</div></article>
    <article class="card"><div class="photo blouse" role="img" aria-label="Produktfoto: Model in olivgrüner Bluse und schwarzer Hose"></div><div class="badge"><span>-31%</span></div><div class="info"><div class="cat">Cardingans</div><div class="title">Storehall - Strukturk<br>leid mit Rückwärtigem...</div><div class="prices">65.00€<span class="now">€ 24.99 €*</span></div><div class="ship">Versand: +5,95</div></div><div class="shop">Zum Shop</div></article>

    <article class="card"><div class="photo cardigan" role="img" aria-label="Produktfoto: Model in weißer Strickjacke und grauer Jeans"></div><div class="badge"><span>-45%</span></div><div class="info"><div class="cat">Cardingans</div><div class="title">Storehall - Strukturk<br>leid mit Rückwärtigem...</div><div class="prices">65.00€<span class="now">€ 24.99 €*</span></div><div class="ship">Versand: +5,95</div></div><div class="shop">Zum Shop</div></article>
    <article class="card"><div class="photo blouse" role="img" aria-label="Produktfoto: Model in olivgrüner Bluse und schwarzer Hose"></div><div class="badge"><span>-31%</span></div><div class="info"><div class="cat">Cardingans</div><div class="title">Storehall - Strukturk<br>leid mit Rückwärtigem...</div><div class="prices">65.00€<span class="now">€ 24.99 €*</span></div><div class="ship">Versand: +5,95</div></div><div class="shop">Zum Shop</div></article>
    <article class="card"><div class="photo cardigan" role="img" aria-label="Produktfoto: Model in weißer Strickjacke und grauer Jeans"></div><div class="badge"><span>-45%</span></div><div class="info"><div class="cat">Cardingans</div><div class="title">Storehall - Strukturk<br>leid mit Rückwärtigem...</div><div class="prices">65.00€<span class="now">€ 24.99 €*</span></div><div class="ship">Versand: +5,95</div></div><div class="shop">Zum Shop</div></article>
    <article class="card"><div class="photo blouse" role="img" aria-label="Produktfoto: Model in olivgrüner Bluse und schwarzer Hose"></div><div class="badge"><span>-31%</span></div><div class="info"><div class="cat">Cardingans</div><div class="title">Storehall - Strukturk<br>leid mit Rückwärtigem...</div><div class="prices">65.00€<span class="now">€ 24.99 €*</span></div><div class="ship">Versand: +5,95</div></div><div class="shop">Zum Shop</div></article>

    <article class="card"><div class="photo cardigan" role="img" aria-label="Produktfoto: Model in weißer Strickjacke und grauer Jeans"></div><div class="badge"><span>-45%</span></div><div class="info"><div class="cat">Cardingans</div><div class="title">Storehall - Strukturk<br>leid mit Rückwärtigem...</div><div class="prices">65.00€<span class="now">€ 24.99 €*</span></div><div class="ship">Versand: +5,95</div></div><div class="shop">Zum Shop</div></article>
    <article class="card"><div class="photo blouse" role="img" aria-label="Produktfoto: Model in olivgrüner Bluse und schwarzer Hose"></div><div class="badge"><span>-31%</span></div><div class="info"><div class="cat">Cardingans</div><div class="title">Storehall - Strukturk<br>leid mit Rückwärtigem...</div><div class="prices">65.00€<span class="now">€ 24.99 €*</span></div><div class="ship">Versand: +5,95</div></div><div class="shop">Zum Shop</div></article>
    <article class="card"><div class="photo cardigan" role="img" aria-label="Produktfoto: Model in weißer Strickjacke und grauer Jeans"></div><div class="badge"><span>-45%</span></div><div class="info"><div class="cat">Cardingans</div><div class="title">Storehall - Strukturk<br>leid mit Rückwärtigem...</div><div class="prices">65.00€<span class="now">€ 24.99 €*</span></div><div class="ship">Versand: +5,95</div></div><div class="shop">Zum Shop</div></article>
    <article class="card"><div class="photo blouse" role="img" aria-label="Produktfoto: Model in olivgrüner Bluse und schwarzer Hose"></div><div class="badge"><span>-31%</span></div><div class="info"><div class="cat">Cardingans</div><div class="title">Storehall - Strukturk<br>leid mit Rückwärtigem...</div><div class="prices">65.00€<span class="now">€ 24.99 €*</span></div><div class="ship">Versand: +5,95</div></div><div class="shop">Zum Shop</div></article>
  </main>

  <div class="more">View More Products</div>

  <footer class="footer">
    <div class="brand">velunix</div>
    <p class="blurb">Lorem ipsum dolor sit amet, consectetur adip-isicing elit, sed do eiusmod tempor incididunt ut labore et dolore magna aliqua</p>
    <p class="copy">© Copyright velunix 2012.<br>velunix ist nicht verantwortlich für den Inhalt externer Links.</p>
    <div class="fcol" style="left:545px"><h4>Menu</h4>About Us<br>Services<br>Privacy Police<br>Terms Of Service</div>
    <div class="fcol" style="left:715px"><h4>Links</h4>Kontakt<br>AGB<br>Impressum<br>Nur reduzierte Artikel</div>
    <div class="signup">
      <h4>Get on the list</h4>
      <div class="email"><span>Your Email Address</span><b>Confirm</b></div>
      <h4 class="stay">Stay Connected</h4>
      <div class="fsocial"><i title="Plimbora"></i><i title="zappel"></i><i title="Feed"></i></div>
    </div>
  </footer>

</div>
</body>
</html>
```